I would like a flyer for the ultimate masquarade ball. This will be a PARTY! We need a flyer that will jump out and catch the attention of anyone who sees it. We would like plenty of purple and gold to be used in the flyer. The final design should communicate the ultmate, upscale, classy, exciting masquarade ball ever!

This flyer must be designed for high resolution for printing on 4" x 6" flyers.

Requirements
Must have
• Zeta Kappa Chapter Presents
Lantern Velvet & Ember Masquerade Ball
1 March 2014
8pm - 1am
3-Course Plated Dinner
Cash Bar
RSVP By: 28 Feb 2014
Halvorsen Gaming & Downs, North Banquet Hall
DJ Tavrik
Details & Tickets: http://lanternvelvetemberball.ticketnook.example
More Info? 555-318-7726
Dress Code: Black Tie & Traditional Dress, Costumes & Masks Preferred

```html
<!DOCTYPE html>
<html lang="en">
<head>
<meta charset="utf-8">
<title>Lantern Velvet &amp; Ember Masquerade Ball</title>
<link rel="stylesheet" href="https://fonts.googleapis.com/css2?family=Great+Vibes&family=Cinzel:wght@600&family=Libre+Baskerville:wght@700&display=swap">
<style>
  :root {
    --page: #ffffff;
    --night: #050307;
    --plum: #3a0f45;
    --violet: #6a1f86;
    --orchid: #8e2fa8;
    --gold: #f3dc2a;
    --amber: #f0c419;
    --pale-gold: #f6e47e;
    --silver: #8a8a8a;
    --ivory: #f4efe6;
  }
  * { margin: 0; padding: 0; box-sizing: border-box; }
  html, body { width: 850px; height: 1200px; overflow: hidden; background: var(--page); }
  .canvas { position: relative; width: 850px; height: 1200px; background: var(--page); }

  .flyer {
    position: absolute; left: 55px; top: 40px; width: 745px; height: 1120px;
    overflow: hidden;
    background:
      radial-gradient(ellipse 55% 14% at 20% 4%, rgba(106,31,134,.75), transparent 70%),
      radial-gradient(ellipse 45% 10% at 85% 3%, rgba(106,31,134,.6), transparent 70%),
      radial-gradient(ellipse 70% 6% at 40% 58%, rgba(106,31,134,.7), transparent 75%),
      linear-gradient(to bottom, var(--night) 0%, var(--night) 53%, var(--plum) 60%, var(--violet) 70%, var(--orchid) 100%);
    text-align: center;
  }

  .presenter {
    position: absolute; top: 64px; left: 0; right: 0;
    font-family: "Great Vibes", cursive; color: var(--gold);
    font-size: 48px; line-height: 1;
  }
  .presents {
    position: absolute; top: 130px; left: 0; right: 0;
    font-family: "Great Vibes", cursive; color: var(--gold);
    font-size: 28px;
  }

  .title {
    position: absolute; top: 166px; left: 0; right: 0;
    font-family: "Great Vibes", cursive; font-weight: 400;
    color: var(--gold); font-size: 84px; line-height: 84px;
  }
  .title .line { display: block; position: relative; }
  .title .amp {
    position: absolute; left: 50%; top: 46px; transform: translateX(-50%);
    color: var(--silver); font-size: 84px; z-index: 0; opacity: .9;
  }
  .title .word { position: relative; z-index: 1; }

  .mask-art {
    position: absolute; left: 30px; top: 405px; width: 690px; height: 215px;
    background:
      radial-gradient(ellipse 22% 40% at 50% 50%, rgba(142,47,168,.9), transparent 75%),
      radial-gradient(ellipse 18% 35% at 22% 48%, rgba(240,196,25,.55), transparent 75%),
      radial-gradient(ellipse 18% 35% at 78% 48%, rgba(240,196,25,.55), transparent 75%),
      radial-gradient(ellipse 50% 45% at 50% 50%, rgba(80,120,40,.35), transparent 80%);
  }

  .when {
    position: absolute; left: 0; right: 0;
    font-family: "Cinzel", serif; font-weight: 600;
    color: var(--ivory); font-size: 31px; line-height: 1; letter-spacing: 1.5px;
  }
  .when.date { top: 610px; }
  .when.time { top: 654px; }

  .details {
    position: absolute; top: 701px; left: 0; right: 0;
    list-style: none;
    font-family: "Libre Baskerville", serif; font-weight: 700;
    color: var(--amber); font-size: 21px; line-height: 29.3px;
  }
  .details .label { color: var(--pale-gold); }
</style>
</head>
<body>
<div class="canvas">
  <main class="flyer">
    <p class="presenter">Zeta Kappa Chapter</p>
    <p class="presents">Presents</p>

    <h1 class="title">
      <span class="line"><span class="word">Lantern Velvet</span><span class="amp">&amp;</span></span>
      <span class="line"><span class="word">Ember Masquerade</span></span>
      <span class="line"><span class="word">Ball</span></span>
    </h1>

    <div class="mask-art" role="img" aria-label="Ornate purple, gold and green feathered masquerade mask with swirling filigree"></div>

    <p class="when date">1 MARCH 2014</p>
    <p class="when time">8PM - 1AM</p>

    <ul class="details">
      <li>3-Course Plated Dinner</li>
      <li>Cash Bar</li>
      <li><span class="label">RSVP By:</span> 28 Feb 2014</li>
      <li>Halvorsen Gaming &amp; Downs, North Banquet Hall</li>
      <li>DJ Tavrik</li>
      <li class="label">Details &amp; Tickets:</li>
      <li>http://lanternvelvetemberball.ticketnook.example</li>
      <li class="label">More Info?</li>
      <li>555-318-7726</li>
      <li class="label">Dress Code:</li>
      <li>Black Tie &amp; Traditional Dress,</li>
      <li>Costumes &amp; Masks Preferred</li>
    </ul>
  </main>
</div>
</body>
</html>
```